VORLEN Website Design

We need a website designed for our company VORLEN. We are a luxury lifestyle club that will provide benefits and services for our members. The site should be clean & sleek, preferably using black and white (or darker colors). (example sites: brimvale.example, tusko.example)

Here is a link of a sample page I did using wix. (https://pelmundry4.sitebuild.example/mypage) This can be used to get a general idea.

Target Market(s)

Upper Middle Class in the United States

Number of Pages Required

5+ page

Font styles to use
Sans Serif
Other font styles liked:
• Arial (or other similar fonts)

Requirements
Must have
• A clean design that is eye-catching and speaks to our company.
Nice to have
• Ideas for copy.

```html
<!DOCTYPE html>
<html lang="en">
<head>
<meta charset="utf-8">
<title>VORLEN — A Members Only Lifestyle Club</title>
<link rel="stylesheet" href="https://fonts.googleapis.com/css2?family=Source+Sans+3:wght@300;400;600;700&family=Montserrat:wght@400;500&display=swap">
<style>
  :root{
    --bg:#000;
    --panel:#2a2a2a;
    --white:#fff;
    --muted:#9a9a9a;
    --muted-2:#7c7c7c;
    --soft:#b8b8b8;
    --blue:#2a9ee0;
    --footer-bar:#2e2e33;
    --cat-music:#1530e0;
    --cat-sports:#0f8a68;
    --cat-party:#f36b2e;
    --cat-fitness:#1d6ed2;
    --cat-pets:#3bcb3a;
    --cat-game:#b5197c;
    --cat-education:#3651ea;
  }
  *{box-sizing:border-box;margin:0;padding:0}
  html,body{width:1200px;height:2990px;overflow:hidden;background:var(--bg);color:var(--white);font-family:"Source Sans 3",Arial,sans-serif}
  .page{position:relative;width:1200px;height:2990px}
  .abs{position:absolute}

  /* header */
  .site-header{left:0;top:0;width:1200px;height:76px;background:var(--bg)}
  .brand{left:80px;top:10px;width:112px;height:58px;background:#1c1c22;display:flex;align-items:center;justify-content:center;font-size:27px;font-weight:400;letter-spacing:1px}
  .main-nav{top:31px;left:588px;display:flex;font-size:13px;font-weight:400;text-transform:uppercase;white-space:nowrap}
  .main-nav a{color:var(--white);text-decoration:none;margin-right:29px}
  .main-nav a.services{margin-right:31px;margin-left:14px}
  .search-icon{left:1092px;top:26px}

  /* hero */
  .hero{left:0;top:76px;width:1200px;height:538px;background:
    radial-gradient(ellipse 40% 55% at 30% 30%,rgba(180,130,110,.45),transparent 70%),
    radial-gradient(ellipse 35% 50% at 80% 40%,rgba(150,110,150,.45),transparent 70%),
    linear-gradient(180deg,#3b2740 0%,#4a2f58 50%,#2c1a38 100%)}
  .hero-title{left:84px;top:236px;font-size:46px;font-weight:600;line-height:60px;letter-spacing:-0.5px}
  .hero-text{left:88px;top:374px;width:480px;font-size:13.5px;line-height:22px}
  .btn{display:flex;align-items:center;justify-content:center;font-size:14px;font-weight:600;color:var(--white);white-space:nowrap}
  .btn-watch{left:88px;top:450px;width:212px;height:56px;background:var(--blue)}
  .btn-visit{left:316px;top:450px;width:194px;height:56px;border:2px solid var(--white);text-transform:uppercase}
  .btn svg{margin-right:8px}

  /* about */
  .about-photo{left:86px;top:692px;width:504px;height:472px;background:
    radial-gradient(ellipse 50% 45% at 45% 45%,rgba(190,150,90,.55),transparent 70%),
    linear-gradient(135deg,#2a4a9a 0%,#3a3a6a 50%,#1a1a2e 100%)}
  .about-panel{left:590px;top:692px;width:522px;height:472px;background:var(--panel)}
  .about-title{left:664px;top:772px;font-size:58px;font-weight:600;line-height:72px;white-space:nowrap}
  .about-text{left:670px;top:878px;width:404px;font-size:11px;line-height:21px}
  .btn-learn{left:668px;top:1032px;width:172px;height:44px;border:1px solid var(--white);font-size:13px}

  /* categories */
  .cat-title{left:84px;top:1210px;font-family:"Montserrat",Arial,sans-serif;font-size:28px;font-weight:400;letter-spacing:.5px}
  .category{width:128px;height:120px;border-radius:50%;display:flex;flex-direction:column;align-items:center;justify-content:center;font-size:12px}
  .category span{margin-top:-8px}

  /* events */
  .events-title{left:86px;top:1456px;font-size:34px;font-weight:700}
  .event{overflow:hidden}
  .event-label{position:absolute;left:14px;right:14px;bottom:14px;display:flex;justify-content:space-between;font-size:12px;font-weight:700;text-transform:uppercase}
  .event-label .rate{display:flex;align-items:center;gap:6px}

  /* gallery */
  .gallery{left:84px;top:2042px;width:1028px;height:458px;background:
    radial-gradient(ellipse 30% 55% at 78% 55%,rgba(200,150,110,.45),transparent 70%),
    linear-gradient(90deg,#141414 0%,#1c1c1c 44%,#3e3030 60%,#5a4050 78%,#4e3070 100%)}
  .gallery-title{left:154px;top:2110px;font-size:35px;font-weight:600;line-height:40px;text-transform:uppercase;letter-spacing:.5px}
  .gallery-text{left:152px;top:2202px;width:420px;font-size:12px;line-height:26px}
  .btn-gallery{left:158px;top:2364px;width:166px;height:44px;border:2px solid var(--white);border-radius:22px;font-size:14px}

  /* footer */
  .genre-links{left:242px;top:2560px;width:718px;display:flex;justify-content:space-between;font-family:"Montserrat",Arial,sans-serif;font-size:11.5px;color:var(--muted)}
  .foot-heading{font-family:"Montserrat",Arial,sans-serif;color:var(--muted-2);font-weight:500}
  .contact-heading{left:140px;top:2652px;font-size:15px}
  .contact-links{left:144px;top:2686px;width:300px;font-size:12px;line-height:24px;color:var(--soft)}
  .genre-heading{left:462px;top:2652px;font-size:11px;letter-spacing:.5px}
  .genre-list{left:462px;top:2688px;width:316px;font-size:10.5px;line-height:21.5px;color:var(--soft)}
  .foot-brand{left:900px;top:2648px;font-size:36px;font-weight:300;letter-spacing:2px}
  .copyright{left:896px;top:2728px;font-size:10.5px;line-height:16px;color:var(--soft)}
  .social{left:890px;top:2772px;display:flex;gap:9px}
  .social span{width:30px;height:30px;border:1.5px solid var(--white);border-radius:50%;display:flex;align-items:center;justify-content:center}
  .social span::after{content:"";width:8px;height:8px;border-radius:50%;background:var(--white)}
  .bottom-bar{left:0;top:2906px;width:1200px;height:84px;background:var(--footer-bar);display:flex;align-items:center;justify-content:center;font-size:10px;color:#a8a8a8}
</style>
</head>
<body>
<div class="page">

  <header class="site-header abs">
    <div class="brand abs">VORLEN</div>
    <nav class="main-nav abs">
      <a href="#">Home</a><a href="#">About</a><a class="services" href="#">Services and Benefits</a><a href="#">Apply</a><a href="#">Contact</a>
    </nav>
    <svg class="search-icon abs" width="24" height="24" viewBox="0 0 24 24" fill="none" stroke="#fff" stroke-width="2"><circle cx="10" cy="10" r="7"/><line x1="15" y1="15" x2="21" y2="21"/></svg>
  </header>

  <section class="hero abs" role="img" aria-label="Friends laughing and toasting with drinks at a lively club night"></section>
  <h1 class="hero-title abs">VORLEN A Members Only<br>Lifestyle Club</h1>
  <p class="hero-text abs">Lorem Ipsum is simply dummy text of the printing and typesetting industry.<br>Lorem Ipsum has been the industry's standard dummy text ever since</p>
  <a class="btn btn-watch abs"><svg width="10" height="12" viewBox="0 0 10 12"><path d="M0 0L10 6L0 12Z" fill="#fff"/></svg>Watch Now</a>
  <a class="btn btn-visit abs">Visit a Club</a>

  <div class="about-photo abs" role="img" aria-label="Women dancing under blue club lights holding champagne"></div>
  <div class="about-panel abs"></div>
  <h2 class="about-title abs">About VORLEN</h2>
  <p class="about-text abs">Lorem Ipsum is simply dummy text of the printing and typesetting industry. Lorem Ipsum has been the industry's standard dummy text ever since the 1500s, when an unknown printer took a galley of type and scrambled it to make a type specimen book. It has survived not only five centuries, but also the leap into electronic typesetting, remaining essentially unchanged. It was popularised in the 1960s with the release of Pressletter sheets containing</p>
  <a class="btn btn-learn abs">Learn More</a>

  <h2 class="cat-title abs">Explore Categories</h2>
  <div class="category abs" style="left:86px;top:1288px;background:var(--cat-music)"><svg width="40" height="40" viewBox="0 0 40 40" fill="none" stroke="#fff" stroke-width="2"><path d="M14 30V8l16-4v22"/><circle cx="10" cy="30" r="4"/><circle cx="26" cy="26" r="4"/></svg><span>Music</span></div>
  <div class="category abs" style="left:234px;top:1288px;background:var(--cat-sports)"><svg width="40" height="40" viewBox="0 0 40 40" fill="none" stroke="#fff" stroke-width="2"><circle cx="20" cy="20" r="14"/><path d="M6 20h28M20 6v28M10 10c6 6 6 14 0 20M30 10c-6 6-6 14 0 20"/></svg><span>Sports</span></div>
  <div class="category abs" style="left:394px;top:1288px;background:var(--cat-party)"><svg width="40" height="40" viewBox="0 0 40 40" fill="none" stroke="#fff" stroke-width="2"><path d="M10 8l4 14-4 12M30 8l-4 14 4 12M8 34h6M26 34h6M20 4v4M16 6l2 3M24 6l-2 3"/></svg><span>Party</span></div>
  <div class="category abs" style="left:540px;top:1288px;background:var(--cat-fitness)"><svg width="44" height="40" viewBox="0 0 44 40" fill="none" stroke="#fff" stroke-width="2"><rect x="6" y="12" width="6" height="16" rx="1"/><rect x="32" y="12" width="6" height="16" rx="1"/><path d="M12 20h20M2 16v8M42 16v8"/></svg><span>Fitness</span></div>
  <div class="category abs" style="left:692px;top:1288px;background:var(--cat-pets)"><svg width="40" height="40" viewBox="0 0 40 40" fill="none" stroke="#fff" stroke-width="2"><ellipse cx="20" cy="26" rx="8" ry="6"/><circle cx="11" cy="16" r="3"/><circle cx="17" cy="10" r="3"/><circle cx="23" cy="10" r="3"/><circle cx="29" cy="16" r="3"/></svg><span>Pets</span></div>
  <div class="category abs" style="left:836px;top:1288px;background:var(--cat-game)"><svg width="40" height="40" viewBox="0 0 40 40" fill="none" stroke="#fff" stroke-width="2"><path d="M28 6c-8 2-14 8-16 16l6 6c8-2 14-8 16-16z"/><circle cx="24" cy="16" r="3"/><path d="M12 22l-6 2 4 4M18 28l-2 6-4-4"/></svg><span>Game</span></div>
  <div class="category abs" style="left:988px;top:1288px;background:var(--cat-education)"><svg width="40" height="40" viewBox="0 0 40 40" fill="none" stroke="#fff" stroke-width="2"><path d="M4 16l16-8 16 8-16 8z"/><path d="M11 20v8c5 4 13 4 18 0v-8M34 17v9"/></svg><span>Education</span></div>

  <h2 class="events-title abs">Most popular Events</h2>
  <div class="event abs" style="left:90px;top:1530px;width:360px;height:440px;background:linear-gradient(180deg,#7fa6d4 0%,#d6e0ea 38%,#e8e8e8 52%,#4a4a4a 72%,#8a1a1a 86%,#2a2a2a 100%)" role="img" aria-label="Guests stepping off a private jet onto a red carpet">
    <div class="event-label"><span>Private Jet Travel</span><span class="rate"><svg width="13" height="12" viewBox="0 0 13 12"><path d="M6.5 12L1 6.5C-1 4 1 0 4 1l2.5 2L9 1c3-1 5 3 3 5.5z" fill="#fff"/></svg>75%</span></div>
  </div>
  <div class="event abs" style="left:464px;top:1530px;width:316px;height:208px;background:linear-gradient(135deg,#1e2026 0%,#6a7078 45%,#c8ccd2 100%)" role="img" aria-label="Hands reviewing financial documents with a pen">
    <div class="event-label"><span>Accounting Services</span><span class="rate"><svg width="13" height="12" viewBox="0 0 13 12"><path d="M6.5 12L1 6.5C-1 4 1 0 4 1l2.5 2L9 1c3-1 5 3 3 5.5z" fill="#fff"/></svg>75%</span></div>
  </div>
  <div class="event abs" style="left:800px;top:1530px;width:316px;height:208px;background:linear-gradient(180deg,#3cb0c8 0%,#1a7a98 55%,#0c4a62 100%)" role="img" aria-label="Diver swimming beside a manta ray in clear blue water">
    <div class="event-label"><span>Experiences</span><span class="rate"><svg width="13" height="12" viewBox="0 0 13 12"><path d="M6.5 12L1 6.5C-1 4 1 0 4 1l2.5 2L9 1c3-1 5 3 3 5.5z" fill="#fff"/></svg>75%</span></div>
  </div>
  <div class="event abs" style="left:464px;top:1760px;width:316px;height:210px;background:linear-gradient(135deg,#141c34 0%,#2e3e62 50%,#141c34 100%)" role="img" aria-label="Stock market chart on a screen">
    <div class="event-label"><span>Investment Services</span><span class="rate"><svg width="13" height="12" viewBox="0 0 13 12"><path d="M6.5 12L1 6.5C-1 4 1 0 4 1l2.5 2L9 1c3-1 5 3 3 5.5z" fill="#fff"/></svg>75%</span></div>
  </div>
  <div class="event abs" style="left:800px;top:1760px;width:316px;height:210px;background:linear-gradient(135deg,#3a4a2e 0%,#6a5a44 50%,#2e2e24 100%)" role="img" aria-label="Friends sharing food at an outdoor table">
    <div class="event-label"><span>Private Events</span><span class="rate"><svg width="13" height="12" viewBox="0 0 13 12"><path d="M6.5 12L1 6.5C-1 4 1 0 4 1l2.5 2L9 1c3-1 5 3 3 5.5z" fill="#fff"/></svg>75%</span></div>
  </div>

  <section class="gallery abs" role="img" aria-label="Group of friends raising bottles together at a party"></section>
  <h2 class="gallery-title abs">Amazing<br>VORLEN Gallery</h2>
  <p class="gallery-text abs">Lorem Ipsum is simply dummy text of the printing and typesetting industry. Lorem Ipsum has been the industry's standard dummy text ever since the 1500s, when an unknown printer took a galley of type and scrambled it to make a type specimen book. It has survived not only five centuries, but also the leap into electronic type-setting, remaining essentially unchanged. I</p>
  <a class="btn btn-gallery abs"><svg width="10" height="12" viewBox="0 0 10 12"><path d="M0 0L10 6L0 12Z" fill="#fff"/></svg>Watch Now</a>

  <footer>
    <nav class="genre-links abs"><span>Action Movies</span><span>Comedy Movies</span><span>Romance Movies</span><span>Thriller Movies</span><span>Horror Movies</span><span>Adult Movies</span><span>Family Movies</span></nav>
    <h3 class="foot-heading contact-heading abs">Questions ? Contact us</h3>
    <p class="contact-links abs">FAQ | Help | CentreAccount | Media CentreInvestor<br>Relations Jobs | Ways to Watch<br>Terms of UsePrivacy</p>
    <h3 class="foot-heading genre-heading abs">BEST LANGUAGE GENRE MOVIES</h3>
    <p class="genre-list abs">Hindi Comedy Movies | Hindi Action Movies | English Animated Movies | English Fantasy Movies | English Comedy Movies | English Action Movies | Tamil Action Movies | Tamil Comedy Movies | Telugu Action Movies | Gujrati Comedy Movies | Marathi Drama Movies | Marathi Comedy Movies | Hindi Animated Movies</p>
    <div class="foot-brand abs">VORLEN</div>
    <p class="copyright abs">Copyright 2018 Technologies.<br>All rights reserved.</p>
    <div class="social abs" aria-label="Social links"><span></span><span></span><span></span><span></span></div>
    <div class="bottom-bar abs">no endorsement of the artist shall be implied. Unauthorized use is prohibited and punishable by law.</div>
  </footer>

</div>
</body>
</html>
```